Kestrel Motorworks Card

Our company is an offroad fabrication shop that does everything from product installs to complete turnkey offroad racers. We are looking to generate new business cards for the 2014 Lords of the Canyon race in February. This is one of the largest offroad races in the country. We would like to see designs that incorporate the colors used in our logo - black, red, and white.

Industry/Entity Type

Shop

Contact Information for Business Card

KESTREL Motorworks, 2873 Marwood Ln. Houston, TX, 713-452-3071, www.kestrelmotorworks.example, Leon Farrowby, Owen Tilsley, Owners.

Requirements
Nice to have
• Would like to see the Logo full size on the back size of the car.

```html
<!DOCTYPE html>
<html lang="en">
<head>
<meta charset="utf-8">
<title>Kestrel Motorworks Business Card</title>
<link rel="stylesheet" href="https://fonts.googleapis.com/css2?family=Oswald:wght@500;700&family=Arimo:wght@400&display=swap">
<style>
  :root {
    --bg: #e6e4e1;
    --card-dark: #1c2427;
    --card-mid: #2d3b41;
    --card-light: #3b4b52;
    --panel-edge: #56676e;
    --red: #e0232b;
    --stripe: #e84a2c;
    --white: #f4f4f4;
    --grey-text: #8d9397;
    --texture: #161c1e;
  }
  * { margin: 0; padding: 0; box-sizing: border-box; }
  html, body { width: 1200px; height: 1000px; overflow: hidden; background: var(--bg); }
  .canvas { position: relative; width: 1200px; height: 1000px; }

  .card {
    position: absolute; left: 215px; width: 770px; height: 440px;
    border-radius: 6px; overflow: hidden;
    background: linear-gradient(160deg, var(--card-light) 0%, var(--card-mid) 45%, var(--card-dark) 100%);
    box-shadow: 0 10px 28px rgba(0,0,0,.28);
  }
  .card--front { top: 40px; }
  .card--back { top: 520px; }

  /* Front */
  .front__texture {
    position: absolute; left: 0; top: 0; width: 70px; height: 100%;
    background: linear-gradient(180deg, var(--texture), #202a2d);
  }
  .front__panel {
    position: absolute; left: 70px; top: 0; width: 640px; height: 300px;
    border-radius: 0 0 40px 0;
    background: linear-gradient(165deg, #34444a, #263135);
    border-right: 2px solid var(--panel-edge); border-bottom: 2px solid var(--panel-edge);
  }
  .front__brand {
    position: absolute; left: 130px; top: 80px; width: 540px;
    display: flex; align-items: center; gap: 20px;
  }
  .front__mark { width: 26px; height: 26px; background: var(--red); flex: none; }
  .front__name {
    font-family: "Oswald", sans-serif; font-weight: 700; font-size: 62px;
    line-height: 1.1; color: var(--red); letter-spacing: 1px;
  }
  .front__stripes { position: absolute; left: 330px; top: 320px; display: flex; gap: 14px; }
  .front__stripes span { width: 24px; height: 34px; background: var(--stripe); }

  /* Back */
  .back__panel {
    position: absolute; left: 0; top: 0; width: 770px; height: 285px;
    border-radius: 0 0 40px 0;
    background: linear-gradient(165deg, #3a4a50, #2a363b);
    border-bottom: 2px solid var(--panel-edge);
  }
  .back__lower {
    position: absolute; left: 0; top: 285px; width: 770px; height: 155px;
    background: linear-gradient(180deg, #1f282b, #161d1f);
  }
  .back__names {
    position: absolute; left: 60px; top: 44px; width: 650px; height: 80px;
    border: 2px solid var(--white);
    display: flex; align-items: center; justify-content: center;
    font-family: "Oswald", sans-serif; font-weight: 700; font-size: 40px; line-height: 1;
    color: var(--white); text-transform: uppercase; white-space: nowrap;
  }
  .back__role, .back__company {
    position: absolute; left: 0; width: 770px; text-align: center; line-height: 1;
    font-family: "Oswald", sans-serif; font-weight: 500; color: var(--red); text-transform: uppercase;
    white-space: nowrap;
  }
  .back__role { top: 152px; font-size: 36px; letter-spacing: 34px; padding-left: 34px; }
  .back__company { top: 218px; font-size: 30px; letter-spacing: 16px; padding-left: 16px; }
  .back__contact {
    position: absolute; left: 60px; top: 305px; list-style: none;
    font-family: "Arimo", sans-serif; font-size: 26px; color: var(--grey-text);
  }
  .back__contact li { display: flex; align-items: center; gap: 18px; height: 40px; white-space: nowrap; }
  .back__contact svg { width: 22px; height: 22px; fill: var(--red); flex: none; }
</style>
</head>
<body>
<main class="canvas">
  <section class="card card--front" aria-label="Card front">
    <div class="front__texture" role="img" aria-label="Dark perforated texture strip"></div>
    <div class="front__panel"></div>
    <div class="front__brand">
      <span class="front__mark"></span>
      <span class="front__name">KESTREL Motorworks</span>
    </div>
    <div class="front__stripes"><span></span><span></span><span></span><span></span><span></span></div>
  </section>

  <section class="card card--back" aria-label="Card back">
    <div class="back__panel"></div>
    <div class="back__lower"></div>
    <div class="back__names">Leon Farrowby - Owen Tilsley</div>
    <div class="back__role">Owners</div>
    <div class="back__company">Kestrel Motorworks</div>
    <ul class="back__contact">
      <li>
        <svg viewBox="0 0 24 24" aria-hidden="true"><path d="M12 2a7 7 0 0 0-7 7c0 5 7 13 7 13s7-8 7-13a7 7 0 0 0-7-7zm0 9.5A2.5 2.5 0 1 1 12 6.5a2.5 2.5 0 0 1 0 5z"/></svg>
        2873 Marwood Ln. Houston, TX
      </li>
      <li>
        <svg viewBox="0 0 24 24" aria-hidden="true"><path d="M6.6 10.8a15 15 0 0 0 6.6 6.6l2.2-2.2a1 1 0 0 1 1-.25 11.4 11.4 0 0 0 3.6.57 1 1 0 0 1 1 1V20a1 1 0 0 1-1 1A17 17 0 0 1 3 4a1 1 0 0 1 1-1h3.5a1 1 0 0 1 1 1c0 1.25.2 2.450.57 3.6a1 1 0 0 1-.25 1z"/></svg>
        713-452-3071
      </li>
      <li>
        <svg viewBox="0 0 24 24" aria-hidden="true"><path d="M12 3 2 12h3v8h5v-6h4v6h5v-8h3z"/></svg>
        www.kestrelmotorworks.example
      </li>
    </ul>
  </section>
</main>
</body>
</html>
```